I need the Scorecard I've developed for my staff to be produced into a visually engaging piece that will encourage the staff to utilize it on a daily basis. I'm thinking it could be 5x7 in size so that it isn't too cumbersome, but I'm open to different layouts.
I have multiple other departments that will need Scorecards created for them as well, but each one will contain task specific questions for each department.

```html
<!DOCTYPE html>
<html lang="en">
<head>
<meta charset="utf-8">
<title>Receptionist Daily Excellence Scorecard</title>
<link rel="stylesheet" href="https://fonts.googleapis.com/css2?family=Gelasio:wght@400;700&family=Arimo:wght@400&display=swap">
<style>
  :root {
    --indigo: #3f3a8a;
    --magenta: #9b3a8f;
    --label-blue: #45409a;
    --lavender: #f2f1f7;
    --white: #ffffff;
    --ink: #1e1e24;
    --rule: #a9a7b6;
    --backdrop: #6e4a2c;
    --star-gold: #f2b632;
  }
  * { margin: 0; padding: 0; box-sizing: border-box; }
  html, body { width: 918px; height: 1200px; overflow: hidden; }
  body { background: var(--backdrop); position: relative; font-family: "Arimo", Arial, sans-serif; color: var(--ink); }
  .scorecard { position: absolute; left: 75px; top: 66px; width: 768px; height: 1074px; background: var(--lavender); overflow: hidden; }
  .abs { position: absolute; }
  .title-band { left: 0; top: 0; width: 768px; height: 65px; background: var(--indigo); }
  .title { left: 28px; top: 9px; font-family: "Gelasio", Georgia, serif; font-size: 35px; color: var(--white); white-space: nowrap; }
  .title-rule-white { left: 0; top: 65px; width: 768px; height: 3px; background: var(--white); }
  .title-rule-magenta { left: 0; top: 68px; width: 768px; height: 3px; background: var(--magenta); }
  .strip { left: 0; width: 768px; height: 43px; background: var(--white); }
  .heading { left: 27px; font-family: "Gelasio", Georgia, serif; font-weight: 700; font-size: 22px; color: var(--magenta); white-space: nowrap; }
  .heading small { font-size: 15px; }
  .field-label { font-family: "Gelasio", Georgia, serif; font-size: 18px; white-space: nowrap; }
  .rule { height: 1px; background: var(--rule); }
  .scale-text { font-family: "Gelasio", Georgia, serif; font-size: 16px; white-space: nowrap; }
  .col-head { font-family: "Gelasio", Georgia, serif; font-size: 16px; color: var(--label-blue); white-space: nowrap; }
  .task { left: 28px; font-size: 14.5px; white-space: nowrap; }
  .option { width: 210px; }
  .option-circle { position: absolute; left: 0; top: 3px; width: 13px; height: 13px; border: 1.3px solid var(--ink); border-radius: 50%; }
  .option-name { margin-left: 26px; font-size: 15px; color: var(--label-blue); }
  .option-desc { margin-left: 26px; margin-top: 4px; font-size: 12px; line-height: 1.42; }
  .prompt { font-size: 13px; color: var(--label-blue); white-space: nowrap; }
  .prompt b { color: var(--magenta); font-family: "Gelasio", Georgia, serif; font-size: 17px; margin-right: 4px; }
  .mark-label { font-size: 13px; color: var(--label-blue); white-space: nowrap; }
  .mark-label span { font-size: 9.5px; }
  .footer { left: 0; top: 880px; }
  .footer-text { font-family: "Gelasio", Georgia, serif; color: var(--white); white-space: nowrap; }
  .footer-rule { height: 1px; background: #8d89c4; }
  .award-art { left: 12px; top: 913px; width: 57px; height: 46px; border-radius: 4px; background: linear-gradient(135deg, #f2b632, #f6c6a8); }
</style>
</head>
<body>
<main class="scorecard">
  <div class="abs title-band"></div>
  <h1 class="abs title">Receptionist Daily Excellence Scorecard</h1>
  <div class="abs title-rule-white"></div>
  <div class="abs title-rule-magenta"></div>

  <!-- Identity row -->
  <span class="abs field-label" style="left:28px;top:94px">Name:</span>
  <div class="abs rule" style="left:90px;top:113px;width:168px"></div>
  <span class="abs field-label" style="left:278px;top:94px">Date:</span>
  <div class="abs rule" style="left:329px;top:113px;width:168px"></div>
  <span class="abs field-label" style="left:517px;top:94px">Location:</span>
  <div class="abs rule" style="left:604px;top:113px;width:160px"></div>

  <!-- Rating scale -->
  <div class="abs strip" style="top:138px"></div>
  <h2 class="abs heading" style="top:145px">Please Rate Yourself For Each Task</h2>
  <svg class="abs" style="left:661px;top:145px" width="86" height="30" viewBox="0 0 86 30" fill="none" stroke="#9b3a8f" stroke-width="1.6" stroke-linejoin="round">
    <path d="M8 15l2 4 4.4.6-3.2 3 .8 4.4-4-2.1-4 2.1.8-4.4-3.2-3 4.4-.6z"/>
    <path d="M24 10l2.3 4.6 5 .7-3.6 3.5.9 5-4.6-2.4-4.6 2.4.9-5-3.6-3.5 5-.7z"/>
    <path d="M43 3l2.8 5.6 6.2.9-4.5 4.4 1.1 6.2-5.6-2.9-5.6 2.9 1.1-6.2-4.5-4.4 6.2-.9z"/>
    <path d="M62 10l2.3 4.6 5 .7-3.6 3.5.9 5-4.6-2.4-4.6 2.4.9-5-3.6-3.5 5-.7z"/>
    <path d="M78 15l2 4 4.4.6-3.2 3 .8 4.4-4-2.1-4 2.1.8-4.4-3.2-3 4.4-.6z"/>
  </svg>
  <span class="abs scale-text" style="left:28px;top:194px">1 = Needs Improvement</span>
  <span class="abs scale-text" style="left:305px;top:194px">3 = Meets Expectations</span>
  <span class="abs scale-text" style="left:617px;top:194px">5 = Excellent</span>

  <!-- Call handling -->
  <div class="abs strip" style="top:242px"></div>
  <h2 class="abs heading" style="top:249px">Call Handling &amp; First Call Intake</h2>
  <svg class="abs" style="left:652px;top:245px" width="80" height="38" viewBox="0 0 80 38" fill="none" stroke="#9b3a8f" stroke-width="1.6" stroke-linecap="round">
    <circle cx="17" cy="12" r="7"/>
    <path d="M8 12a9 9 0 0 1 18 0"/>
    <path d="M26 13v4h-6"/>
    <path d="M3 34c0-8 6-12 14-12s14 4 14 12z"/>
    <circle cx="30" cy="30" r="4"/>
    <path d="M28.3 30l1.2 1.2 2.2-2.4"/>
    <path d="M55 6c-3 1-4 5-2 10 3 8 9 14 17 17 5 2 9 1 10-2l-5-5-4 3c-4-2-8-6-10-10l3-4z"/>
    <path d="M74 6l-8 8M66 8v6h6"/>
  </svg>
  <span class="abs col-head" style="left:28px;top:296px">Task</span>
  <span class="abs col-head" style="left:434px;top:296px">Self-Rating (1-5)</span>
  <span class="abs col-head" style="left:587px;top:296px">Notes / Issues</span>
  <span class="abs task" style="top:328px">Answered 90%+ calls within 3 rings</span>
  <span class="abs task" style="top:361px">Maintained empathy and professionalism</span>
  <span class="abs task" style="top:395px">Accurately completed all First Call fields</span>
  <span class="abs task" style="top:427px">Worked within Receptionist role</span>
  <div class="abs rule" style="left:426px;top:343px;width:136px"></div>
  <div class="abs rule" style="left:573px;top:343px;width:137px"></div>
  <div class="abs rule" style="left:426px;top:376px;width:136px"></div>
  <div class="abs rule" style="left:573px;top:376px;width:137px"></div>
  <div class="abs rule" style="left:426px;top:410px;width:136px"></div>
  <div class="abs rule" style="left:573px;top:410px;width:137px"></div>
  <div class="abs rule" style="left:426px;top:442px;width:136px"></div>
  <div class="abs rule" style="left:573px;top:442px;width:137px"></div>

  <!-- Status summary -->
  <div class="abs strip" style="top:472px"></div>
  <h2 class="abs heading" style="top:479px">Daily Status Summary <small>(Circle One)</small></h2>
  <svg class="abs" style="left:719px;top:475px" width="30" height="32" viewBox="0 0 30 32" fill="#9b3a8f" stroke="#9b3a8f" stroke-width="1.5">
    <rect x="2" y="20" width="4" height="9" stroke="none"/>
    <rect x="9" y="16" width="4" height="13" stroke="none"/>
    <rect x="16" y="12" width="4" height="17" stroke="none"/>
    <rect x="23" y="8" width="4" height="21" stroke="none"/>
    <path d="M1 31h28" fill="none"/>
    <path d="M3 15L24 3M19 2.5l5 .5-1.5 4.5" fill="none"/>
  </svg>
  <div class="abs option" style="left:40px;top:530px"><i class="option-circle"></i><div class="option-name">Excellent</div><div class="option-desc">All key duties completed, proactive, calm under pressure</div></div>
  <div class="abs option" style="left:263px;top:530px"><i class="option-circle"></i><div class="option-name">Satisfactory</div><div class="option-desc">Most duties completed, minor follow-up needed</div></div>
  <div class="abs option" style="left:515px;top:530px"><i class="option-circle"></i><div class="option-name">Needs Support</div><div class="option-desc">Missed urgent duties, accuracy or stress issues</div></div>

  <!-- Reflection -->
  <div class="abs strip" style="top:629px"></div>
  <h2 class="abs heading" style="left:33px;top:636px">Daily Reflection</h2>
  <svg class="abs" style="left:693px;top:632px" width="54" height="38" viewBox="0 0 54 38" fill="none" stroke="#9b3a8f" stroke-width="1.6">
    <path d="M3 34A24 24 0 0 1 51 34"/>
    <path d="M10 34A17 17 0 0 1 44 34"/>
    <path d="M7 20l5 3M15 10l3 5M27 5v6M39 10l-3 5M47 20l-5 3"/>
    <circle cx="27" cy="28" r="8"/>
    <circle cx="27" cy="26" r="2.5"/>
    <path d="M22.5 33a5 5 0 0 1 9 0"/>
  </svg>
  <span class="abs prompt" style="left:30px;top:680px"><b>?</b>What went well today?</span>
  <span class="abs prompt" style="left:253px;top:680px"><b>?</b>Any issues or barriers to note?</span>
  <span class="abs prompt" style="left:508px;top:680px"><b>?</b>Support needed from supervisor?</span>
  <div class="abs rule" style="left:47px;top:725px;width:136px"></div>
  <div class="abs rule" style="left:47px;top:748px;width:136px"></div>
  <div class="abs rule" style="left:271px;top:725px;width:182px"></div>
  <div class="abs rule" style="left:271px;top:748px;width:182px"></div>
  <div class="abs rule" style="left:523px;top:725px;width:203px"></div>
  <div class="abs rule" style="left:523px;top:748px;width:203px"></div>

  <!-- Stars & flags -->
  <div class="abs strip" style="top:769px"></div>
  <h2 class="abs heading" style="top:776px">Stars &amp; Flags <small>(Supervisor Use Only)</small></h2>
  <svg class="abs" style="left:26px;top:825px" width="20" height="19" viewBox="0 0 20 19" fill="none" stroke="#f2b632" stroke-width="1.4" stroke-linejoin="round"><path d="M10 1l2.7 5.5 6 .9-4.4 4.2 1 6-5.3-2.8-5.3 2.8 1-6L1.3 7.4l6-.9z"/></svg>
  <span class="abs mark-label" style="left:52px;top:827px">Stars <span>(Excellence or above-and-beyond moments)</span></span>
  <svg class="abs" style="left:414px;top:825px" width="18" height="19" viewBox="0 0 18 19" fill="none" stroke="#45409a" stroke-width="1.4" stroke-linejoin="round"><path d="M2 18V2M2 2h13l-3 4 3 4H2"/></svg>
  <span class="abs mark-label" style="left:437px;top:827px">Flags <span>(Concerns needing follow-up/coaching)</span></span>
  <div class="abs rule" style="left:25px;top:862px;width:324px"></div>
  <div class="abs rule" style="left:25px;top:885px;width:324px"></div>
  <div class="abs rule" style="left:415px;top:864px;width:305px"></div>
  <div class="abs rule" style="left:415px;top:886px;width:305px"></div>

  <!-- Footer -->
  <svg class="abs footer" width="768" height="194" viewBox="0 0 768 194">
    <path d="M0 12C180 0 380 50 560 68C650 76 720 62 768 44V194H0Z" fill="#3f3a8a"/>
    <path d="M230 14C380 30 470 60 560 68C650 76 720 62 768 44" fill="none" stroke="#9b3a8f" stroke-width="9"/>
    <path d="M0 8C180 -4 380 46 560 62C650 70 720 58 768 38" fill="none" stroke="#9b3a8f" stroke-width="1.5"/>
  </svg>
  <div class="abs award-art" role="img" aria-label="Thumbs-up hand with gold stars"></div>
  <span class="abs footer-text" style="left:11px;top:958px;font-size:19px">Manager's Overall Rating</span>
  <span class="abs footer-text" style="left:11px;top:983px;font-size:9.5px">Performance On A 1-5 Scale</span>
  <div class="abs footer-rule" style="left:248px;top:982px;width:178px"></div>
  <span class="abs footer-text" style="left:11px;top:1016px;font-size:12.5px">Receptionist Signature</span>
  <span class="abs footer-text" style="left:230px;top:1016px;font-size:12.5px">Supervisor Signature</span>
  <span class="abs footer-text" style="left:480px;top:1016px;font-size:12.5px">Date</span>
  <div class="abs footer-rule" style="left:11px;top:1063px;width:160px"></div>
  <div class="abs footer-rule" style="left:230px;top:1063px;width:150px"></div>
  <div class="abs footer-rule" style="left:480px;top:1063px;width:202px"></div>
</main>
</body>
</html>
```